Law Firm Needs Brochure Redesign Using New Logo

We are a personal injury law firm that does auto injuries and other personal injury cases. We want a new brochure that has our updated logo and information. Instead of gold and black, we want more navy, as matches the new logo. The Auto Liability portion should read: "(required by the state of Arizona in the amounts of $25,000 per person / $50,000 per accident, but a higher amount may be best )." The other information can remain the same. We'd like the brochure to keep the same professional tone as the previous brochure.
Our website is https://www.marbrenlegal.com/.

```html
<!DOCTYPE html>
<html lang="en">
<head>
<meta charset="utf-8">
<title>Marbren Law – Auto Accident Brochure</title>
<link rel="stylesheet" href="https://fonts.googleapis.com/css2?family=Open+Sans:wght@400;600&display=swap">
<style>
  :root {
    --accent: #9dbbe3;
    --white: #ffffff;
    --navy-ink: #14284a;
    --navy-deep: #07142b;
    --navy: #0f2347;
    --road-top: #13264a;
    --road-mid: #23395f;
    --road-low: #1a2d51;
    --car-hi: #7f93b3;
    --car-mid: #3c5279;
    --paper: #ffffff;
    --page-bg: #ffffff;
  }
  * { box-sizing: border-box; margin: 0; padding: 0; }
  html, body {
    width: 1200px; height: 930px; overflow: hidden;
    background: var(--page-bg);
    font-family: "Open Sans", Arial, sans-serif;
  }
  .brochure { position: relative; width: 1200px; height: 930px; }
  .panel { position: absolute; top: 0; height: 930px; overflow: hidden; }

  /* Left panel: statistics */
  .panel--stats { left: 0; width: 397px; color: var(--white); text-align: center; }
  .road-photo {
    position: absolute; inset: 0;
    background:
      linear-gradient(90deg, rgba(3,10,24,0.45) 0%, rgba(3,10,24,0) 35%, rgba(3,10,24,0) 65%, rgba(3,10,24,0.45) 100%),
      linear-gradient(180deg, var(--road-top) 0%, #1a2e54 30%, var(--road-mid) 60%, var(--road-low) 100%);
  }
  .stat { position: absolute; left: 0; right: 0; }
  .stat__lead { font-size: 17px; letter-spacing: 0.5px; }
  .stat__number { color: var(--accent); font-size: 74px; line-height: 1; font-weight: 400; margin: 4px 0 6px; }
  .stat__text { font-size: 17px; line-height: 1.45; padding: 0 40px; }
  .stat--crashes { top: 176px; }
  .stat--fatalities { top: 398px; }
  .rule { position: absolute; left: 45px; right: 14px; top: 640px; border-top: 1px solid rgba(255,255,255,0.55); }
  .firm-mark { display: flex; align-items: center; gap: 14px; }
  .firm-mark__dot { width: 44px; height: 44px; border-radius: 50%; background: var(--accent); flex: none; }
  .firm-mark__name { color: var(--accent); font-weight: 600; font-size: 30px; letter-spacing: 2px; text-transform: uppercase; white-space: nowrap; }
  .panel--stats .firm-mark { position: absolute; left: 52px; top: 660px; }
  .promise { position: absolute; left: 62px; right: 62px; top: 736px; font-size: 15px; line-height: 1.42; }

  /* Middle panel: mailer */
  .panel--mailer { left: 397px; width: 398px; background: var(--paper); }
  .return-address {
    position: absolute; left: 424px; top: 908px;
    transform-origin: 0 0; transform: rotate(-90deg);
    display: flex; flex-direction: column; align-items: flex-start; gap: 22px;
  }
  .return-address .firm-mark { gap: 10px; }
  .return-address .firm-mark__dot { width: 28px; height: 28px; background: var(--navy); }
  .return-address .firm-mark__name { font-size: 20px; letter-spacing: 1.5px; color: var(--navy); }
  .return-address__lines { font-size: 13px; line-height: 1.6; color: var(--navy-ink); }

  /* Right panel: cover */
  .panel--cover { left: 795px; width: 405px; background: var(--navy-deep); }
  .car-photo {
    position: absolute; left: 0; right: 0; top: 190px; bottom: 0;
    background:
      radial-gradient(ellipse 70% 45% at 75% 40%, var(--car-hi) 0%, var(--car-mid) 35%, rgba(7,20,43,0) 75%),
      radial-gradient(ellipse 60% 35% at 80% 70%, #2c4068 0%, rgba(7,20,43,0) 70%),
      var(--navy-deep);
  }
  .cover__title { position: absolute; left: 58px; top: 54px; color: var(--white); font-size: 25px; line-height: 1.3; font-weight: 400; }
  .cover__subtitle { position: absolute; left: 0; right: 0; top: 124px; text-align: center; padding-left: 40px; color: var(--accent); font-size: 17px; line-height: 1.35; }
  .panel--cover .firm-mark { position: absolute; left: 38px; top: 802px; }
  .panel--cover .firm-mark__dot { width: 62px; height: 62px; }
  .panel--cover .firm-mark__name { font-size: 32px; }
</style>
</head>
<body>
<main class="brochure">

  <section class="panel panel--stats">
    <div class="road-photo" role="img" aria-label="Photo of a two-lane country road lined with trees, in deep navy tones"></div>
    <div class="stat stat--crashes">
      <p class="stat__lead">OVER</p>
      <p class="stat__number">107,000</p>
      <p class="stat__text">crashes will happen in the state of Arizona this year.</p>
    </div>
    <div class="stat stat--fatalities">
      <p class="stat__lead">OVER</p>
      <p class="stat__number">700</p>
      <p class="stat__text">of them will result in fatalities.</p>
    </div>
    <div class="rule"></div>
    <div class="firm-mark">
      <span class="firm-mark__dot"></span>
      <span class="firm-mark__name">Marbren Law</span>
    </div>
    <p class="promise">If we don't win, you don't pay attorney fees. That seems fair to us. Know what's happening with your case, get the answers to your questions and work on getting better with the confidence that you've got an excellent group of people working for you.</p>
  </section>

  <section class="panel panel--mailer"></section>
  <div class="return-address">
    <div class="firm-mark">
      <span class="firm-mark__dot"></span>
      <span class="firm-mark__name">Marbren Law</span>
    </div>
    <p class="return-address__lines">4870 N. 16th Street Suite B310<br>Phoenix AZ 85016</p>
  </div>

  <section class="panel panel--cover">
    <div class="car-photo" role="img" aria-label="Photo of the front of a silver car with its headlight lit, against a dark navy background"></div>
    <h1 class="cover__title">Protect your family in<br>case of a car accident</h1>
    <p class="cover__subtitle">A little knowledge and preparation<br>go a long way</p>
    <div class="firm-mark">
      <span class="firm-mark__dot"></span>
      <span class="firm-mark__name">Marbren Law</span>
    </div>
  </section>

</main>
</body>
</html>
```